New Alcoholic Spiked Seltzer Line

We need a can design for a line of low calorie alcoholic seltzer. This product is a sparkling water and vodka drink with no sugar added in a slim 12 oz can.

This is a lighter, healthier, alternative to the sugary ready-to-drinks on the market. The product contains only 3 ingredients: Vodka, Water and Natural Flavors. It has only 100 calories but still has 5% alcohol, so you don't need to sacrifice alcohol to cut calories.

This product also does not contain any preservatives.

We want this design to communicate the following objectives to the consumer and in this order:

1. Appetizing product
2.Low calorie
3.Communicate the type of beverage (Spiked Seltzer)

The brand name of the product is VELKA.

The flavor of the product needed to be used for the design is Mango-Orange.

Comparable products are:

www.brisavelfizz.example/
https://www.tarnowbubble.example
https://quellrind.example/

The designs should not infringe or copy the creative directions of the products mentionned above. They are only given so that you can better understand the type of product we are developing.

Target Market(s)

Young Professional women between the ages of 25 and 44

Industry/Entity Type

Product

Colors

Designer to choose colors to be used in the design.

Requirements
Must have
• Design extendibility, meaning it can be adapted for other flavors.
• This is a new category in the market we are targeting, so consumers must easily be able to identify what type of product this is.

```html
<!DOCTYPE html>
<html lang="en">
<head>
<meta charset="utf-8">
<title>VELKA Orange &amp; Mango Label</title>
<link rel="stylesheet" href="https://fonts.googleapis.com/css2?family=Montserrat:wght@400;600;700&display=swap">
<style>
  :root {
    --bg-light: #f4f5f6;
    --bg-mid: #d9dcde;
    --label-white: #ffffff;
    --brand-orange: #e07a32;
    --flavor-orange: #e8902a;
    --mango-yellow: #f6c21c;
    --peach: #f0955a;
    --coral: #e9705a;
    --band-orange: #ef9a5c;
  }
  html, body {
    margin: 0;
    padding: 0;
    width: 1200px;
    height: 1200px;
    overflow: hidden;
  }
  body {
    position: relative;
    background: radial-gradient(ellipse at 50% 60%, var(--bg-light) 0%, var(--bg-mid) 100%);
    font-family: "Montserrat", sans-serif;
  }
  p, h1 { margin: 0; }
  .label {
    position: absolute;
    left: 190px;
    top: 190px;
    width: 370px;
    height: 800px;
    background: var(--label-white);
    box-shadow: 0 10px 30px rgba(0,0,0,0.08);
  }
  .label-tagline {
    position: absolute;
    top: 24px;
    left: 0;
    width: 100%;
    text-align: center;
    font-size: 11px;
    font-weight: 700;
    letter-spacing: 0.02em;
    line-height: 14px;
    color: var(--flavor-orange);
  }
  .fruit-wash {
    position: absolute;
    left: 8px;
    top: 126px;
    width: 350px;
    height: 452px;
    border-radius: 48% 52% 46% 54% / 50% 46% 54% 50%;
    background: radial-gradient(ellipse at 50% 30%, var(--coral) 0%, var(--peach) 45%, var(--mango-yellow) 100%);
  }
  .natural-claim {
    position: absolute;
    top: 221px;
    left: 0;
    width: 100%;
    text-align: center;
    font-size: 13px;
    font-weight: 600;
    letter-spacing: 0.3em;
    line-height: 16px;
    color: var(--label-white);
  }
  .label-brand {
    position: absolute;
    top: 300px;
    left: 0;
    width: 100%;
    text-align: center;
    font-size: 80px;
    font-weight: 600;
    letter-spacing: 0.04em;
    line-height: 100px;
    color: var(--label-white);
  }
  .flavor-name {
    position: absolute;
    top: 618px;
    left: 0;
    width: 100%;
    text-align: center;
    font-size: 27px;
    font-weight: 700;
    letter-spacing: 0.08em;
    line-height: 32px;
    color: var(--flavor-orange);
  }
  .stats-band {
    position: absolute;
    top: 690px;
    left: 0;
    width: 100%;
    height: 84px;
    display: flex;
    align-items: center;
    justify-content: space-around;
    background: linear-gradient(90deg, var(--band-orange), var(--coral) 50%, var(--band-orange));
    color: var(--label-white);
  }
  .stat {
    text-align: center;
    width: 33%;
  }
  .stat + .stat { border-left: 1px solid rgba(255,255,255,0.8); }
  .stat-value { font-size: 26px; font-weight: 400; line-height: 1; }
  .stat-unit { font-size: 8px; font-weight: 700; letter-spacing: 0.05em; margin-top: 4px; }
  .lockup {
    position: absolute;
    left: 700px;
    top: 500px;
    width: 460px;
    text-align: center;
    color: var(--brand-orange);
  }
  .lockup-brand {
    font-size: 110px;
    font-weight: 600;
    letter-spacing: 0.04em;
    line-height: 1;
  }
  .lockup-tagline {
    margin-top: 110px;
    font-size: 15px;
    font-weight: 600;
    letter-spacing: 0.06em;
    line-height: 18px;
  }
</style>
</head>
<body>
  <section class="label">
    <p class="label-tagline">LIGHT ON CALORIES, FULL ON FIZZ</p>
    <div class="fruit-wash" role="img" aria-label="Watercolour wash of orange and mango tones"></div>
    <p class="natural-claim">100% NATURAL</p>
    <h1 class="label-brand">VELKA</h1>
    <p class="flavor-name">ORANGE &amp; MANGO</p>
    <div class="stats-band">
      <div class="stat"><div class="stat-value">100</div><div class="stat-unit">CALORIES</div></div>
      <div class="stat"><div class="stat-value">0</div><div class="stat-unit">ADDED<br>SUGAR</div></div>
      <div class="stat"><div class="stat-value">5%</div><div class="stat-unit">ALC./VOL</div></div>
    </div>
  </section>

  <section class="lockup">
    <div class="lockup-brand">VELKA</div>
    <p class="lockup-tagline">LIGHT ON CALORIES, FULL ON FIZZ</p>
  </section>
</body>
</html>
```